Business Card for Professional Photographer

I'm looking for an eye catching modern clean design that compliments my logo/ website fonts & colours.
I specialise in architecture, corporate & commercial photography so I'm marketing to professional clients rather than portrait / wedding clients.

I would prefer to not have a solid black design.

My logo brand guide is as follows :

Main front font. : Reislust
Main font colour : #fff
Slogan front font : Ubuntu Bold
Monogram front font : Venti Medium
Container colour : #fff

I need print ready files in pdf .png & .eps formats.

Included in the files below are some screen grabs as reference to font & colours etc.

```html
<!DOCTYPE html>
<html lang="en">
<head>
<meta charset="utf-8">
<title>Clear Angle – Business Card</title>
<link rel="stylesheet" href="https://fonts.googleapis.com/css2?family=Ubuntu:wght@300;400;500;700&display=swap">
<style>
  :root {
    --page-bg: #e9e9e9;
    --card-white: #ffffff;
    --gold: #c9965a;
    --gold-light: #dfbb80;
    --gold-dark: #cd9d62;
    --text-dark: #4a4a4a;
    --text-mid: #5a5a5a;
    --white: #ffffff;
  }
  * { box-sizing: border-box; margin: 0; padding: 0; }
  html, body {
    width: 963px; height: 1200px; overflow: hidden;
    background: var(--page-bg);
    font-family: "Ubuntu", sans-serif;
  }
  .canvas { position: relative; width: 963px; height: 1200px; }
  .card {
    position: absolute; left: 61px; width: 840px; height: 478px;
  }
  .card--front { top: 100px; background: var(--card-white); }
  .card--back {
    top: 622px;
    background: linear-gradient(180deg, var(--gold-light) 0%, var(--gold-dark) 100%);
  }

  /* brand lockup */
  .brand { position: absolute; display: flex; align-items: center; }
  .brand__mark { flex: none; border-radius: 50%; }
  .brand__words { display: flex; flex-direction: column; }
  .brand__name {
    font-family: "Ubuntu", sans-serif; font-weight: 300;
    text-transform: uppercase; white-space: nowrap;
  }
  .brand__tagline {
    font-weight: 700; white-space: nowrap;
  }

  .card--front .brand { left: 44px; top: 53px; }
  .card--front .brand__mark {
    width: 84px; height: 84px; border: 3px solid var(--gold);
    margin-right: 18px;
  }
  .card--front .brand__name {
    font-size: 24px; letter-spacing: 3.2px; color: var(--text-mid);
  }
  .card--front .brand__tagline {
    font-size: 7.5px; letter-spacing: 1.6px; color: var(--text-mid); margin-top: 2px;
  }

  .card--back .brand { left: 180px; top: 182px; }
  .card--back .brand__mark {
    width: 126px; height: 126px; border: 4px solid var(--white);
    margin-right: 26px;
  }
  .card--back .brand__name {
    font-size: 32px; letter-spacing: 4.6px; color: var(--white);
  }
  .card--back .brand__tagline {
    font-size: 10px; letter-spacing: 3px; color: var(--white); margin-top: 4px;
  }

  /* contact block */
  .address {
    position: absolute; left: 44px; top: 238px;
    font-size: 19px; line-height: 24px; color: var(--text-dark); font-style: normal;
  }
  .contacts {
    position: absolute; left: 44px; top: 302px; list-style: none;
    font-size: 19px; line-height: 24px; color: var(--text-dark);
  }
  .contacts li { display: flex; align-items: center; }
  .contacts svg { width: 15px; height: 15px; margin-right: 9px; fill: var(--gold); flex: none; }

  .person {
    position: absolute; right: 44px; top: 310px; text-align: right;
  }
  .person__name { font-size: 26px; font-weight: 500; color: var(--gold); }
  .person__title { font-size: 18px; font-weight: 500; color: var(--text-dark); margin-top: 2px; }
</style>
</head>
<body>
<main class="canvas">

  <section class="card card--front" aria-label="Card front">
    <div class="brand">
      <span class="brand__mark"></span>
      <div class="brand__words">
        <span class="brand__name">Clear Angle</span>
        <span class="brand__tagline">Architecture Corporate Commercial</span>
      </div>
    </div>

    <address class="address">1420 Birchwood Drive<br>Juneau, Alaska 99801</address>

    <ul class="contacts">
      <li><svg viewBox="0 0 16 16" aria-hidden="true"><path d="M3.5 1l3 3-1.6 2c.9 1.9 2.3 3.3 4.1 4.2l2-1.6 3 3-1.8 2.4C6.5 13.8 2.2 9.5 1.1 3z"/></svg>555-218-4071</li>
      <li><svg viewBox="0 0 16 16" aria-hidden="true"><path d="M4 0h8v16H4zM5.5 1.5v11h5v-11zM7 13.6h2v1.2H7z" fill-rule="evenodd"/></svg>555-730-6192</li>
      <li><svg viewBox="0 0 16 16" aria-hidden="true"><path d="M4 1h8v4H4zM1 6h14v6h-3v3H4v-3H1zM5.5 10v3.5h5V10z" fill-rule="evenodd"/></svg>555-463-2850</li>
      <li><svg viewBox="0 0 16 16" aria-hidden="true"><path d="M1 3.5h14v9H1zM2.5 5l5.5 4 5.5-4v-.2h-11z" fill-rule="evenodd"/></svg>hello@clearanglestudio.com</li>
      <li><svg viewBox="0 0 16 16" aria-hidden="true"><circle cx="8" cy="8" r="7"/><path d="M8 1v14M1 8h14" stroke="#fff" stroke-width="1"/></svg>www.clearanglestudio.com</li>
    </ul>

    <div class="person">
      <div class="person__name">Daniel Harper</div>
      <div class="person__title">President</div>
    </div>
  </section>

  <section class="card card--back" aria-label="Card back">
    <div class="brand">
      <span class="brand__mark"></span>
      <div class="brand__words">
        <span class="brand__name">Clear Angle</span>
        <span class="brand__tagline">Architecture Corporate Commercial</span>
      </div>
    </div>
  </section>

</main>
</body>
</html>
```